Business Card Re-Design for health practice! Easy on the eye design!

We would like a re-deisgn of our current business care for our Exercise Physiology centre.
Clean fresh and easy on the eye with minimal information other than the essentials. Possible inspirational saying or quote on the back would like a nice touch.
Contact and Address details will need up dating for our practitioners.

Vantrel Exercise Physiology provided health and exercise solutions to help people achieve improved quality of life.

More info.... www.vantrelhealth.net.au
Logo attached and current business card
New Contact Details: U3 84 Kelmore Ridge Road, Dunvale NSW 2417
Card info needed:
Ray Mallon BExPhys ESSAM AEP
Nadine Corwick BExPhys ESSAM AEP

Target Market(s)

Broad 25 to 75yrs both male and female

Industry/Entity Type

Health

Contact Information for Business Card

Logo attached and current business card for all information required

Card info needed:

Requirements
Must have
• Current information on attached card
Nice to have
• Logo colours to be used in the new design
Should not have
• Cluttered

```html
<!DOCTYPE html>
<html lang="en">
<head>
<meta charset="utf-8">
<title>Vantrel Exercise Physiology – Business Card</title>
<link href="https://fonts.googleapis.com/css2?family=Open+Sans:wght@300;400;700&display=swap" rel="stylesheet">
<style>
  :root {
    --stage: #1d1d1d;
    --card: #0c0c0c;
    --card-edge: #161616;
    --green: #6cc04a;
    --green-soft: rgba(108, 192, 74, 0.22);
    --white: #f2f2f2;
    --grey: #b9b9b9;
    --divider: #2a2a2a;
  }
  * { margin: 0; padding: 0; box-sizing: border-box; }
  html, body {
    width: 1200px; height: 900px; overflow: hidden;
    background: var(--stage);
    font-family: "Open Sans", Arial, sans-serif;
  }
  .canvas { position: relative; width: 1200px; height: 900px; }

  .card {
    position: absolute;
    width: 525px; height: 300px;
    background: var(--card);
    border: 1px solid var(--card-edge);
    border-radius: 18px;
    overflow: hidden;
  }

  /* Back side: brand */
  .card--brand { left: 615px; top: 140px; }
  .brand {
    position: absolute; left: 0; right: 0; top: 92px;
    display: flex; align-items: center; justify-content: center; gap: 14px;
  }
  .brand__dot { width: 22px; height: 22px; border-radius: 50%; background: var(--green); }
  .brand__name {
    color: var(--green); font-weight: 300; font-size: 30px; letter-spacing: 1px;
  }
  .tagline {
    position: absolute; left: 0; right: 0; top: 185px;
    text-align: center; color: var(--white); font-size: 14px; font-weight: 400;
  }

  /* Front side: contact */
  .card--contact { left: 60px; top: 470px; }
  .print-mark {
    position: absolute; left: 70px; top: 50px; width: 150px; height: 200px;
    border-radius: 50%;
    background: radial-gradient(ellipse at center, var(--green-soft) 0%, rgba(108,192,74,0.08) 60%, transparent 72%);
  }
  .divider {
    position: absolute; left: 262px; top: 40px; width: 1px; height: 220px;
    background: var(--divider);
  }
  .details { position: absolute; left: 290px; top: 52px; color: var(--white); }
  .details__name { color: var(--green); font-weight: 700; font-size: 21px; line-height: 1.1; }
  .details__creds { font-size: 13px; margin-top: 2px; }
  .details__address { font-size: 13px; line-height: 1.35; margin-top: 14px; }
  .contact-list { list-style: none; margin-top: 14px; font-size: 13px; line-height: 1.45; }
  .contact-list li { display: flex; align-items: center; gap: 8px; }
  .contact-list svg { width: 13px; height: 13px; flex: none; fill: var(--green); }
</style>
</head>
<body>
<main class="canvas">

  <section class="card card--brand" aria-label="Card back">
    <div class="brand">
      <span class="brand__dot"></span>
      <span class="brand__name">Vantrel Exercise Physiology</span>
    </div>
    <p class="tagline">Optimising Health, Quality of Life &amp; Function</p>
  </section>

  <section class="card card--contact" aria-label="Card front">
    <div class="print-mark" role="img" aria-label="Large green line-art brand motif"></div>
    <div class="divider"></div>
    <div class="details">
      <h1 class="details__name">Theo Marsh</h1>
      <p class="details__creds">AEP AES ESSAM</p>
      <p class="details__address">U3 84 Kelmore Ridge Road,<br>Dunvale NSW 2417</p>
      <ul class="contact-list">
        <li>
          <svg viewBox="0 0 16 16" aria-hidden="true"><path d="M3.5 1.5l2.5 0 1.2 3-1.6 1.2c.8 1.7 2 2.9 3.7 3.7l1.2-1.6 3 1.2v2.5c0 .8-.7 1.5-1.5 1.5C6.6 13 3 9.4 2 3c0-.8.7-1.5 1.5-1.5z"/></svg>
          02 5718 3264
        </li>
        <li>
          <svg viewBox="0 0 16 16" aria-hidden="true"><path d="M4 1h8v4H4zM1 6h14v6h-3v3H4v-3H1zM5 10v4h6v-4z"/></svg>
          02 5718 3270
        </li>
        <li>
          <svg viewBox="0 0 16 16" aria-hidden="true"><path d="M1 3h14v10H1zM2.5 4.5v.3L8 9l5.5-4.2v-.3zM2.5 6.6v5h11v-5L8 10.8z"/></svg>
          theo@vantrelhealth.net.au
        </li>
        <li>
          <svg viewBox="0 0 16 16" aria-hidden="true"><path d="M8 1a7 7 0 1 0 0 14A7 7 0 0 0 8 1zm0 1.5c.8 0 1.7 1.6 2 4H6c.3-2.4 1.2-4 2-4zM2.6 6.5h2C4.5 7 4.5 7.5 4.5 8s0 1 .1 1.5h-2a5.6 5.6 0 0 1 0-3zm8.8 0h2a5.6 5.6 0 0 1 0 3h-2c.1-.5.1-1 .1-1.5s0-1-.1-1.5zM6 9.5h4c-.3 2.4-1.2 4-2 4s-1.7-1.6-2-4z"/></svg>
          www.vantrelhealth.net.au
        </li>
      </ul>
    </div>
  </section>

</main>
</body>
</html>
```